diesel mechanic business card design

summit diesel is a new and upcoming business we are looking for some bad ass designs to help get us started we offer 24 hour road service, off road recovery, welding and custom fabrications we are diesel mechanics so our design should be bold and eye catching flames wrenches engine parts are cool we work in an industrial environment around heavy trucks and equipment this in not a quikko oil we fix it all nothing is to big or to small the colors red and black are always a plus but we are open to anything you guys can come up with ready set go

Target Market(s)

other small business primarily trucking and transportation companys

Industry/Entity Type

Business

Contact Information for Business Card

company name Sumitt diesel truck & trailer repair / address 14 rear north holbrin ave taylor PA 18503 / ownersAdam DeLuccie 570-555-0143 / Curtis Lavandel 570-555-0178 E mail brentmarvoski@mailvex.com fax 570-555-0192

Requirements
Nice to have
• industrial modern design
Should not have
• rainbows butterfly's unicorns or cupcakes

```html
<!DOCTYPE html>
<html lang="en">
<head>
<meta charset="utf-8">
<title>Sumitt diesel truck &amp; trailer repair – business card</title>
<link rel="stylesheet" href="https://fonts.googleapis.com/css2?family=Berkshire+Swash&family=Arimo:wght@400&display=swap">
<style>
  :root {
    --page-bg: #e6e4e0;
    --card-bg: #ffffff;
    --card-edge: #f3f3f4;
    --ink: #1c1c1c;
    --ink-soft: #3a3a3a;
    --truck-blue: #2f5fc4;
    --truck-blue-dark: #1b3b86;
    --truck-ghost: #d9dced;
    --shadow: rgba(0, 0, 0, 0.18);
  }
  * { box-sizing: border-box; margin: 0; padding: 0; }
  html, body {
    width: 1200px; height: 902px; overflow: hidden;
    background: var(--page-bg);
  }
  .canvas { position: relative; width: 1200px; height: 902px; }

  .card {
    position: absolute;
    width: 630px; height: 360px;
    background: linear-gradient(135deg, var(--card-edge), var(--card-bg) 55%);
    box-shadow: 0 10px 28px var(--shadow);
    overflow: hidden;
  }
  .card--back { left: 50px; top: 50px; }
  .card--front { left: 520px; top: 492px; }

  .photo { position: absolute; }
  .photo--ghost {
    left: 20px; top: 40px; width: 400px; height: 300px;
    background: radial-gradient(ellipse at 45% 50%, var(--truck-ghost), rgba(255,255,255,0) 70%);
  }
  .photo--truck {
    left: 30px; top: 120px; width: 360px; height: 235px;
    background: linear-gradient(160deg, var(--truck-blue) 20%, var(--truck-blue-dark) 75%, #9aa2ad);
    border-radius: 40px 24px 10px 10px;
  }

  .title {
    position: absolute; right: 40px; top: 34px;
    font-family: "Berkshire Swash", cursive;
    font-size: 34px; line-height: 1.0; color: var(--ink);
    text-align: right;
  }
  .title span { display: block; }

  .contact {
    position: absolute; right: 40px; top: 170px;
    font-family: "Arimo", sans-serif; color: var(--ink-soft);
    font-size: 17px; text-align: right; line-height: 1.55;
  }
  .contact__row { display: flex; justify-content: flex-end; align-items: center; gap: 8px; }
  .contact__row svg { width: 16px; height: 14px; }
  .contact__row--address { padding-right: 24px; }

  .owners {
    position: absolute; right: 40px; top: 150px;
    font-family: "Arimo", sans-serif; color: var(--ink-soft);
    text-align: right;
  }
  .owner { margin-bottom: 26px; }
  .owner__name { font-size: 22px; line-height: 1.1; }
  .owner__role { font-size: 12px; }
  .owner__phone { font-size: 17px; }
</style>
</head>
<body>
<main class="canvas">

  <section class="card card--back" aria-label="Card back">
    <div class="photo photo--ghost" role="img" aria-label="Faint photo of a semi truck cab in the background"></div>
    <h1 class="title"><span>Sumitt diesel truck</span><span>&amp; trailer repair</span></h1>
    <div class="contact">
      <p class="contact__row">570-555-0192
        <svg viewBox="0 0 16 14" aria-label="fax"><rect x="4" y="0" width="8" height="5" fill="none" stroke="#1c1c1c" stroke-width="1.5"/><rect x="1" y="5" width="14" height="6" fill="#1c1c1c"/><rect x="4" y="9" width="8" height="5" fill="#fff" stroke="#1c1c1c" stroke-width="1.5"/></svg>
      </p>
      <p class="contact__row">brentmarvoski@mailvex.com
        <svg viewBox="0 0 16 14" aria-label="email"><rect x="1" y="2" width="14" height="10" fill="none" stroke="#1c1c1c" stroke-width="1.5"/><path d="M1 2 L8 8 L15 2" fill="none" stroke="#1c1c1c" stroke-width="1.5"/></svg>
      </p>
      <p class="contact__row contact__row--address">14 rear north holbrin ave taylor PA 18503</p>
    </div>
  </section>

  <section class="card card--front" aria-label="Card front">
    <div class="photo photo--truck" role="img" aria-label="Photo of a blue semi truck tractor"></div>
    <h2 class="title"><span>Sumitt diesel truck</span><span>&amp; trailer repair</span></h2>
    <div class="owners">
      <div class="owner">
        <p class="owner__name">Brent Marvoski</p>
        <p class="owner__role">owner</p>
        <p class="owner__phone">570-555-0143</p>
      </div>
      <div class="owner">
        <p class="owner__name">Curtis Lavandel</p>
        <p class="owner__role">owner</p>
        <p class="owner__phone">570-555-0178</p>
      </div>
    </div>
  </section>

</main>
</body>
</html>
```